Coralbay Realty Letterhead

Coralbay Realty Guan
418 Maru Tasi Loop, Ste B207
Tumon, GU. 96928

Industry/Entity Type

Real Estate

Font styles to use
Serif

Colors

Designer to choose colors to be used in the design.

```html
<!DOCTYPE html>
<html lang="en">
<head>
<meta charset="utf-8">
<title>Coralbay Realty Letterhead</title>
<link href="https://fonts.googleapis.com/css2?family=Montserrat:wght@400;500;600&family=Didact+Gothic&family=Open+Sans:wght@600&display=swap" rel="stylesheet">
<style>
  :root {
    --backdrop: #e3e4e6;
    --paper: #ffffff;
    --brand-blue: #0792d1;
    --sky-blue: #5cbfe8;
    --sun-orange: #f6ae3f;
    --text-grey: #6f6f71;
    --date-grey: #737476;
    --ink: #1d1d1d;
  }
  * { margin: 0; padding: 0; box-sizing: border-box; }
  html, body {
    width: 1023px; height: 1200px; overflow: hidden;
    background: var(--backdrop);
  }
  .letterhead {
    position: absolute; left: 84px; top: 0;
    width: 855px; height: 1200px;
    background: var(--paper);
    overflow: hidden;
    font-family: "Didact Gothic", "Century Gothic", sans-serif;
    color: var(--text-grey);
  }
  .brand-mark {
    position: absolute; left: 56px; top: 118px;
    display: flex; align-items: center; gap: 10px;
    font-family: "Montserrat", sans-serif;
    font-weight: 500; font-size: 30px; letter-spacing: 1px;
    color: var(--sky-blue);
  }
  .brand-mark .dot {
    width: 22px; height: 22px; border-radius: 50%;
    background: var(--sky-blue);
  }
  .header-rule {
    position: absolute; left: 56px; top: 170px;
    width: 584px; height: 1.2px; background: var(--brand-blue);
  }
  .office {
    position: absolute; right: 60px; top: 111px;
    text-align: right; font-family: "Montserrat", sans-serif;
  }
  .office-name { font-weight: 600; font-size: 19px; color: var(--brand-blue); line-height: 26px; }
  .office-line { font-size: 16px; line-height: 19.5px; color: var(--text-grey); }
  .sender { position: absolute; left: 56px; top: 290px; font-family: "Montserrat", sans-serif; }
  .sender-name { font-weight: 600; font-size: 26px; color: var(--sky-blue); line-height: 32px; margin-bottom: 6px; }
  .sender-line { font-size: 14.5px; line-height: 18px; margin-bottom: 8.5px; }
  .sender-address { font-size: 14.5px; line-height: 18.5px; }
  .letter-date {
    position: absolute; right: 60px; top: 396px;
    font-family: "Open Sans", sans-serif; font-weight: 600;
    font-size: 16px; color: var(--date-grey);
  }
  .body-copy {
    position: absolute; left: 56px; width: 744px;
    font-size: 13.9px; line-height: 18.7px; text-align: justify;
  }
  .para-one { top: 454px; }
  .para-two { top: 585px; }
  .para-three { top: 716px; }
  .signoff-title {
    position: absolute; right: 74px; top: 918px;
    font-family: "Montserrat", sans-serif; font-size: 19px; color: var(--text-grey);
  }
  .signature {
    position: absolute; left: 607px; top: 968px; width: 174px; height: 108px;
    background: linear-gradient(120deg, #f4f4f4, #e9e9e9);
  }
  .corner-artwork {
    position: absolute; left: 0; bottom: 0; width: 413px; height: 158px;
    background: linear-gradient(100deg, var(--brand-blue) 0%, var(--brand-blue) 62%, var(--sun-orange) 100%);
  }
</style>
</head>
<body>
  <main class="letterhead">
    <div class="brand-mark"><span class="dot"></span>CORALBAY REALTY</div>
    <div class="header-rule"></div>

    <address class="office" style="font-style:normal">
      <div class="office-name">Coralbay Realty Guan</div>
      <div class="office-line">418 Maru Tasi Loop, Ste B207</div>
      <div class="office-line">Tumon, GU. 96928</div>
    </address>

    <section class="sender">
      <h1 class="sender-name">MARA DELACRUZ</h1>
      <p class="sender-line">0671-555-214</p>
      <p class="sender-line">hello@coralbayrealty.example</p>
      <p class="sender-address">77 Harbor View Ln. Suite<br>310 Hagåtña, GU 96910</p>
    </section>

    <p class="letter-date">12 December, 2023</p>

    <p class="body-copy para-one">Lorem ipsum dolor sit amet, consectetuer adipiscing elit, sed diam nonummy nibh euismod tincidunt ut laoreet dolore magna aliquam erat volutpat. Ut wisi enim ad minim veniam, quis nostrud exerci tation ullamcorper suscipit lobortis nisl ut aliquip ex ea commodo consequat. Duis autem vel eum iriure dolor in hendrerit in vulputate velit esse molestie consequat, vel illum dolore eu feugiat nulla facilisis at vero eros et accumsan et iusto odio dignissim qui blandit praesent luptatum zzril delenit augue duis dolore te feugait nulla facilisi.</p>

    <p class="body-copy para-two">Lorem ipsum dolor sit amet, cons ectetuer adipiscing elit, sed diam nonummy nibh euismod tincidunt ut laoreet dolore magna aliquam erat volutpat. Ut wisi enim ad minim veniam, quis nostrud exerci tation ullamcorper suscipit lobortis nisl ut aliquip ex ea commodo consequat.<br>Lorem ipsum dolor sit amet, consectetuer adipiscing elit, sed diam nonummy nibh euismod tincidunt ut laoreet dolore magna aliquam erat</p>

    <p class="body-copy para-three">Lorem ipsum dolor sit amet, cons ectetuer adipiscing elit, sed diam nonummy nibh euismod tincidunt ut laoreet dolore magna aliquam erat volutpat. Ut wisi enim ad minim veniam, quis nostrud exerci tation ullamcorper suscipit lobortis nisl ut aliquip ex ea commodo consequat. Lorem ipsum dolor sit zamet, consectetuer adipiscing elit, sed diam nonummy nibh euismod tincidunt ut laoreet dolore magna aliquam erat volutpat. Ut wisi enim ad minim veniam, quis nostrud exerci tation ullamcorper suscipit lobortis nisl ut aliquip ex ea commodo consequat. Duis autem vel eum iriure.</p>

    <p class="signoff-title">Managing Director</p>
    <div class="signature" role="img" aria-label="Handwritten signature of the managing director"></div>

    <div class="corner-artwork" role="img" aria-label="Decorative illustration of blue house rooftops in front of an orange setting sun"></div>
  </main>
</body>
</html>
```